Business Card for my New Brokerage

Looking to get a business card design for my new Real Estate Brokerage.
I want it with Picture, Phone Number, Email, Website, Office Address
Name and Designation. Please add logo too.

Target Market(s)

Real Estate Investors or Home Buyers

Industry/Entity Type

Real Estate

Contact Information for Business Card

Name, Email, Phone Number, website, email, office address

Colors
EB3D1F
EC4F4E
F09395
F8D3D4
FCEDEE

Requirements
Must have
• Minimalistic, Clean, Modern, Photo
Nice to have
• White and Red Colors

```html
<!DOCTYPE html>
<html lang="en">
<head>
<meta charset="UTF-8">
<title>Ember Realty Inc – Business Card</title>
<link href="https://fonts.googleapis.com/css2?family=Open+Sans:wght@400;600;700&display=swap" rel="stylesheet">
<style>
  :root {
    --page-bg: #e6e4e1;
    --card-black: #0e0e0f;
    --brand-red: #eb3d1f;
    --accent-red: #ec4f4e;
    --text-white: #f2f2f2;
    --text-soft: #c9c9c9;
    --glow: rgba(120, 100, 70, 0.18);
  }
  * { margin: 0; padding: 0; box-sizing: border-box; }
  html, body {
    width: 1200px; height: 800px; overflow: hidden;
    background: var(--page-bg);
    font-family: "Open Sans", Arial, sans-serif;
  }
  .stage {
    width: 1200px; height: 800px;
    display: flex; align-items: center; justify-content: center; gap: 60px;
  }
  .card {
    position: relative;
    width: 525px; height: 300px;
    background: var(--card-black);
    border-radius: 4px;
    overflow: hidden;
    box-shadow: 0 10px 24px rgba(0,0,0,0.25);
  }

  /* brand wordmark */
  .wordmark { color: var(--brand-red); line-height: 1; }
  .wordmark__name { display: block; font-weight: 700; letter-spacing: 1px; }
  .wordmark__sub { display: block; font-weight: 700; letter-spacing: 5px; margin-top: 4px; }

  /* contact side */
  .card--contact .wordmark { position: absolute; left: 40px; top: 36px; }
  .card--contact .wordmark__name { font-size: 46px; }
  .card--contact .wordmark__sub { font-size: 13px; }

  .contact-list {
    position: absolute; left: 40px; top: 138px;
    color: var(--text-white); font-size: 14px; line-height: 21px;
  }
  .contact-list__row { display: flex; align-items: center; gap: 8px; }
  .contact-list__icon { width: 13px; height: 13px; flex: none; }
  .contact-list__address { padding-left: 0; margin-bottom: 2px; }

  .faint-mark {
    position: absolute; right: 60px; bottom: 20px;
    width: 190px; height: 190px; border-radius: 50%;
    background: radial-gradient(circle, var(--glow), transparent 70%);
  }
  .holder {
    position: absolute; right: 40px; bottom: 62px; text-align: left;
  }
  .holder__name {
    color: var(--brand-red); font-weight: 700; font-size: 19px; letter-spacing: 0.5px;
  }
  .holder__title { color: var(--text-white); font-size: 16px; font-weight: 600; }

  /* logo side */
  .card--logo .wordmark {
    position: absolute; left: 50%; top: 50%; transform: translate(-50%, -50%);
    text-align: center;
  }
  .card--logo .wordmark__name { font-size: 68px; }
  .card--logo .wordmark__sub { font-size: 16px; letter-spacing: 8px; }

  .edge-bar { position: absolute; background: var(--brand-red); }
  .edge-bar--top { left: 0; top: 0; width: 8px; height: 58px; }
  .edge-bar--bottom { right: 0; bottom: 0; width: 8px; height: 58px; }
</style>
</head>
<body>
<main class="stage">

  <section class="card card--contact">
    <div class="wordmark">
      <span class="wordmark__name">EMBER</span>
      <span class="wordmark__sub">REALTY INC</span>
    </div>

    <div class="contact-list">
      <div class="contact-list__address">Ember Realty Inc<br>48 Cedar Ridge Lane<br>Maple Grove, ON L6T 3K8</div>
      <div class="contact-list__row">
        <svg class="contact-list__icon" viewBox="0 0 16 16"><path fill="var(--brand-red)" d="M3 1l3 3-2 2c1 2 3 4 6 6l2-2 3 3-2 2C7 15 1 9 1 3z"/></svg>
        <span>+15550142873</span>
      </div>
      <div class="contact-list__row">
        <svg class="contact-list__icon" viewBox="0 0 16 16"><rect x="1" y="3" width="14" height="10" rx="1" fill="var(--brand-red)"/><path d="M1.5 4l6.5 5 6.5-5" stroke="var(--card-black)" stroke-width="1.4" fill="none"/></svg>
        <span>hello@emberrealty.com</span>
      </div>
      <div class="contact-list__row">
        <svg class="contact-list__icon" viewBox="0 0 16 16"><circle cx="8" cy="8" r="6.5" fill="none" stroke="var(--brand-red)" stroke-width="1.5"/><ellipse cx="8" cy="8" rx="2.8" ry="6.5" fill="none" stroke="var(--brand-red)" stroke-width="1.2"/><path d="M1.5 8h13" stroke="var(--brand-red)" stroke-width="1.2"/></svg>
        <span>www.emberrealty.com</span>
      </div>
    </div>

    <div class="faint-mark" aria-hidden="true"></div>
    <div class="holder">
      <div class="holder__name">MARCUS HALE</div>
      <div class="holder__title">Managing Director</div>
    </div>
  </section>

  <section class="card card--logo">
    <span class="edge-bar edge-bar--top"></span>
    <div class="wordmark">
      <span class="wordmark__name">EMBER</span>
      <span class="wordmark__sub">REALTY INC</span>
    </div>
    <span class="edge-bar edge-bar--bottom"></span>
  </section>

</main>
</body>
</html>
```